Business Card Design

My company is a health food catering and delivery business. Our colours are a bright turquiose green/blue, black, white and natural brown based beige. I would like the front of my card (working from the outside in; with a turquoise green boarder -quite thick, with a thin black line separating the turquoise boarder from the beige inside the remaining space of the front of the card with my logo in the centre. This should be all that appears on the front.

On the back I would like all the information displayed above on the beige coloured card, with the blurb in the bright turquoise and my contact information in black please. I would like my business name central - Harvest Crown Kitchen and immediately below with a right alignment - ...Dine like a Monarch
Below this should follow all that I have displayed above with a left alignment.

Target Market(s)

Cafes, restaurants, individuals, buying agents & super markets

Industry/Entity Type

Catering

Contact Information for Business Card

BACK OF BUSINESS CARD:
Harvest Crown Kitchen
...Dine like a Monarch
Deliciously healthy foods - free from gluten, lactose, cane sugar, trans-fat, GMO corn, soy & rice, no artificial flavours, colours or preservatives.
Prepared fresh from locally sourced ingredients, delivered to your door! For individuals, families, corporate, cafes, restaurants & event catering for Toowoomba & surrounds!

PH: 0491 538 207 // orders@harvestcrownkitchen.example
www.harvestcrownkitchen.example
www.socialpage.example/harvestcrownkitchen

Requirements
Must have
• Please supply a modern, easy to read text that will blend nicely with my logo text.
Nice to have
• I really want my business cards to stand out as these will be the template for brochures, menus and website designers to draw inspiration from!
Should not have
• Please do not use Arial, Tahoma or Times Roman text.

```html
<!DOCTYPE html>
<html lang="en">
<head>
<meta charset="utf-8">
<title>Harvest Crown Kitchen — Business Card</title>
<link rel="stylesheet" href="https://fonts.googleapis.com/css2?family=Lobster&family=Cabin:wght@400;600&display=swap">
<style>
  :root {
    --turquoise: #72cbbf;
    --ink: #2a2524;
    --beige: #eedcbb;
    --cream: #f5ecdc;
    --backdrop: #e9e6e1;
    --art-tone: #d9c6a3;
  }
  * { box-sizing: border-box; margin: 0; padding: 0; }
  html, body { width: 1200px; height: 1000px; overflow: hidden; }
  body { background: var(--backdrop); position: relative; }

  .card {
    position: absolute;
    background: var(--turquoise);
    box-shadow: 0 4px 10px rgba(0,0,0,0.25);
  }
  .card__inner {
    position: absolute;
    border: 2px solid var(--ink);
    background: var(--beige);
    overflow: hidden;
  }

  /* Back of card */
  .card--back { left: 405px; top: 63px; width: 700px; height: 432px; }
  .card--back .card__inner { left: 28px; top: 27px; width: 645px; height: 378px; }

  .back__header { height: 124px; position: relative; }
  .brand-name {
    font-family: "Lobster", cursive;
    font-weight: 400;
    font-size: 40px;
    color: var(--ink);
    text-align: center;
    padding-top: 18px;
    line-height: 1.1;
  }
  .brand-tagline {
    font-family: "Lobster", cursive;
    font-size: 23px;
    color: var(--ink);
    position: absolute;
    right: 154px;
    top: 70px;
  }
  .back__blurb {
    height: 148px;
    background: var(--cream);
    font-family: "Cabin", sans-serif;
    font-size: 18.5px;
    line-height: 22.5px;
    color: var(--ink);
    text-align: center;
    padding: 16px 50px 0;
  }
  .back__contact {
    display: flex;
    justify-content: space-between;
    gap: 24px;
    padding: 25px 14px 0 14px;
    font-family: "Cabin", sans-serif;
    font-weight: 600;
    font-size: 15px;
    line-height: 25px;
    color: var(--ink);
    white-space: nowrap;
  }
  .contact__col--right { text-align: right; }

  /* Front of card */
  .card--front { left: 108px; top: 521px; width: 698px; height: 430px; }
  .card--front .card__inner { left: 24px; top: 24px; width: 650px; height: 382px; }

  .front__artwork {
    position: absolute;
    left: 158px; top: 56px;
    width: 370px; height: 210px;
    border-radius: 8px;
    background: radial-gradient(ellipse at 50% 45%, var(--art-tone), var(--beige) 75%);
  }
  .front__name {
    position: absolute;
    left: 0; right: 0; top: 272px;
    text-align: center;
    font-family: "Lobster", cursive;
    font-size: 44px;
    color: var(--ink);
  }
</style>
</head>
<body>

  <section class="card card--back" aria-label="Back of business card">
    <div class="card__inner">
      <header class="back__header">
        <h1 class="brand-name">Harvest Crown Kitchen</h1>
        <p class="brand-tagline">...Dine like a Monarch</p>
      </header>
      <p class="back__blurb">Deliciously healthy foods - free from gluten, lactose, cane sugar, trans-fat, GMO corn, soy &amp; rice, no artificial flavours, colours or preservatives. Prepared fresh from locally sourced ingredients, delivered to your door! For individuals, families, corporate, cafes, restaurants &amp; event catering for Toowoomba &amp; surrounds!</p>
      <div class="back__contact">
        <div class="contact__col">
          <p>Phone: 0491 538 207</p>
          <p>www.harvestcrownkitchen.example</p>
        </div>
        <div class="contact__col contact__col--right">
          <p>orders@harvestcrownkitchen.example</p>
          <p>www.socialpage.example/harvestcrownkitchen</p>
        </div>
      </div>
    </div>
  </section>

  <section class="card card--front" aria-label="Front of business card">
    <div class="card__inner">
      <div class="front__artwork" role="img" aria-label="Line illustration of a cheerful chef in a toque holding a whisk and a frying pan"></div>
      <p class="front__name">Harvest Crown Kitchen</p>
    </div>
  </section>

</body>
</html>
```